Veltrano - Mechanic/Collision Center Business Card

We're looking for a business card design for our mechanic/ collision repair shop.

Can be with colours or monochromatic.

See the attached files.

Many thanks

```html
<!DOCTYPE html>
<html lang="pt">
<head>
<meta charset="utf-8">
<title>Veltrano – Business Cards</title>
<link rel="stylesheet" href="https://fonts.googleapis.com/css2?family=Montserrat:wght@400;700;800&display=swap">
<style>
  :root {
    --bg: #ebeae8;
    --blue: #00aee9;
    --grey: #7d7b7c;
    --navy: #15192b;
    --white: #ffffff;
    --text: #2a2a2a;
    --muted: #6f6f6f;
  }
  * { box-sizing: border-box; margin: 0; padding: 0; }
  html, body { width: 1200px; height: 861px; overflow: hidden; }
  body {
    background: var(--bg);
    font-family: "Montserrat", Arial, sans-serif;
    color: var(--text);
  }
  .sheet {
    display: grid;
    grid-template-columns: 490px 490px;
    grid-template-rows: 300px 300px;
    gap: 60px 70px;
    justify-content: center;
    align-content: center;
    width: 1200px;
    height: 861px;
  }
  .card {
    position: relative;
    width: 490px;
    height: 300px;
    border-radius: 4px;
    box-shadow: 0 6px 18px rgba(0,0,0,0.12);
    overflow: hidden;
  }
  .card--blue { background: var(--blue); }
  .card--grey { background: var(--grey); }
  .card--back { background: var(--white); }

  .front-mark {
    position: absolute;
    inset: 0;
    display: flex;
    align-items: center;
    justify-content: center;
    gap: 16px;
  }
  .front-mark__dot {
    width: 34px; height: 34px; border-radius: 50%;
    background: var(--navy);
  }
  .front-mark__name {
    font-weight: 800;
    font-size: 52px;
    letter-spacing: 3px;
    text-transform: uppercase;
    color: var(--navy);
  }

  .back-holder {
    position: absolute;
    left: 36px;
    top: 44px;
  }
  .back-holder__name { font-weight: 700; font-size: 17px; color: var(--navy); }
  .back-holder__role { font-size: 13px; color: var(--muted); margin-top: 3px; }

  .back-mark {
    position: absolute;
    left: 230px;
    top: 40px;
    display: flex;
    align-items: center;
    gap: 8px;
  }
  .back-mark__dot { width: 14px; height: 14px; border-radius: 50%; background: var(--navy); }
  .back-mark__name {
    font-weight: 800; font-size: 27px; letter-spacing: 1.5px;
    text-transform: uppercase; color: var(--navy);
  }

  .contact {
    position: absolute;
    left: 230px;
    top: 112px;
    list-style: none;
    font-size: 13px;
    line-height: 1.35;
    color: var(--text);
  }
  .contact__item { display: flex; align-items: flex-start; gap: 9px; margin-bottom: 6px; }
  .contact__icon { flex: none; width: 14px; height: 14px; margin-top: 2px; }
</style>
</head>
<body>
<main class="sheet">

  <section class="card card--blue" aria-label="Card front, blue">
    <div class="front-mark">
      <span class="front-mark__dot"></span>
      <span class="front-mark__name">Veltrano</span>
    </div>
  </section>

  <section class="card card--back" aria-label="Card back, company">
    <div class="back-holder">
      <p class="back-holder__name">Veltrano, LDA</p>
    </div>
    <div class="back-mark">
      <span class="back-mark__dot"></span>
      <span class="back-mark__name">Veltrano</span>
    </div>
    <ul class="contact">
      <li class="contact__item">
        <svg class="contact__icon" viewBox="0 0 14 14"><circle cx="7" cy="7" r="7" fill="#00aee9"/><path d="M7 3a2.4 2.4 0 0 0-2.4 2.4C4.6 7.3 7 10.5 7 10.5s2.4-3.2 2.4-5.1A2.4 2.4 0 0 0 7 3zm0 3.3a.9.9 0 1 1 0-1.8.9.9 0 0 1 0 1.8z" fill="#fff"/></svg>
        <span>Rua do Vale Novo, 42<br>1900-210 Lisboa</span>
      </li>
      <li class="contact__item">
        <svg class="contact__icon" viewBox="0 0 14 14"><circle cx="7" cy="7" r="7" fill="#00aee9"/><path d="M4.8 3.6l1.1 1.6-.7.8a5 5 0 0 0 2.8 2.8l.8-.7 1.6 1.1-.6 1.1C6.9 10.3 3.7 7.1 3.7 4.2z" fill="#fff"/></svg>
        <span>+351 210555014</span>
      </li>
      <li class="contact__item">
        <svg class="contact__icon" viewBox="0 0 14 14"><circle cx="7" cy="7" r="7" fill="#00aee9"/><rect x="3.6" y="4.6" width="6.8" height="4.8" fill="#fff"/><path d="M3.6 4.6L7 7.3l3.4-2.7" stroke="#00aee9" stroke-width=".8" fill="none"/></svg>
        <span>oficina@veltrano.pt</span>
      </li>
      <li class="contact__item">
        <svg class="contact__icon" viewBox="0 0 14 14"><circle cx="7" cy="7" r="7" fill="#00aee9"/></svg>
        <span>www.veltrano.pt/social</span>
      </li>
    </ul>
  </section>

  <section class="card card--grey" aria-label="Card front, grey">
    <div class="front-mark">
      <span class="front-mark__dot"></span>
      <span class="front-mark__name">Veltrano</span>
    </div>
  </section>

  <section class="card card--back" aria-label="Card back, personal">
    <div class="back-holder">
      <p class="back-holder__name">Rui Matos</p>
      <p class="back-holder__role">Manager</p>
    </div>
    <div class="back-mark">
      <span class="back-mark__dot"></span>
      <span class="back-mark__name">Veltrano</span>
    </div>
    <ul class="contact">
      <li class="contact__item">
        <svg class="contact__icon" viewBox="0 0 14 14"><circle cx="7" cy="7" r="7" fill="#00aee9"/><path d="M7 3a2.4 2.4 0 0 0-2.4 2.4C4.6 7.3 7 10.5 7 10.5s2.4-3.2 2.4-5.1A2.4 2.4 0 0 0 7 3zm0 3.3a.9.9 0 1 1 0-1.8.9.9 0 0 1 0 1.8z" fill="#fff"/></svg>
        <span>Rua do Vale Novo, 42<br>1900-210 Lisboa</span>
      </li>
      <li class="contact__item">
        <svg class="contact__icon" viewBox="0 0 14 14"><circle cx="7" cy="7" r="7" fill="#00aee9"/><rect x="4.8" y="3.2" width="4.4" height="7.6" rx=".8" fill="#fff"/><circle cx="7" cy="9.6" r=".5" fill="#00aee9"/></svg>
        <span>+351 910555027</span>
      </li>
      <li class="contact__item">
        <svg class="contact__icon" viewBox="0 0 14 14"><circle cx="7" cy="7" r="7" fill="#00aee9"/><rect x="3.6" y="4.6" width="6.8" height="4.8" fill="#fff"/><path d="M3.6 4.6L7 7.3l3.4-2.7" stroke="#00aee9" stroke-width=".8" fill="none"/></svg>
        <span>oficina@veltrano.pt</span>
      </li>
      <li class="contact__item">
        <svg class="contact__icon" viewBox="0 0 14 14"><circle cx="7" cy="7" r="7" fill="#00aee9"/></svg>
        <span>www.veltrano.pt/social</span>
      </li>
    </ul>
  </section>

</main>
</body>
</html>
```